Business Card Design with new logo

Dorian Pelleway 4172
E 118th St Veyton, IL 62091
Cell: 217-555-0193
pellewayrestoration@mailvane.test

Classic Car Restoration Services Buy Sell Trade Consign

Dorian Pelleway 9698
Cell: 217-555-0193

```html
<!DOCTYPE html>
<html lang="en">
<head>
<meta charset="utf-8">
<title>Pelleway Restoration – Business Card</title>
<link rel="stylesheet" href="https://fonts.googleapis.com/css2?family=Crimson+Pro:wght@500;600&family=Racing+Sans+One&display=swap">
<style>
  :root {
    --page: #b9c6cc;
    --card: #141518;
    --card-edge: #0b0c0e;
    --red: #d21f26;
    --red-dark: #8e1116;
    --panel: #6d7378;
    --panel-edge: #5a5f63;
    --headline: #c9cdd0;
    --ink: #141414;
  }
  * { box-sizing: border-box; margin: 0; padding: 0; }
  html, body { width: 1200px; height: 1200px; overflow: hidden; }
  body { background: var(--page); position: relative; font-family: "Crimson Pro", serif; }

  .card {
    position: absolute; top: 250px; width: 398px; height: 699px;
    background: linear-gradient(180deg, #1a1b1e, var(--card) 40%, var(--card-edge));
    box-shadow: 0 6px 14px rgba(0,0,0,.25);
    overflow: hidden;
  }
  .card--front { left: 138px; }
  .card--back { left: 663px; }

  .tread {
    position: absolute; left: 0; width: 100%;
    background: linear-gradient(180deg, var(--red) 0%, var(--red-dark) 45%, var(--red) 55%, var(--red-dark) 100%);
  }

  /* front */
  .brand {
    position: absolute; left: 0; right: 0; top: 120px;
    display: flex; flex-direction: column; align-items: center; gap: 16px;
  }
  .brand__mark { width: 46px; height: 46px; border-radius: 50%; background: var(--red); }
  .brand__name {
    color: var(--red); font-weight: 600; font-size: 34px; letter-spacing: 1px; text-align: center; line-height: 1.1;
  }

  /* back */
  .headline {
    position: absolute; left: 0; right: 0; text-align: center; white-space: nowrap;
    font-family: "Racing Sans One", sans-serif; color: var(--headline);
  }
  .headline--title { top: 10px; font-size: 39px; line-height: 43px; }
  .headline--services { top: 101px; font-size: 28px; line-height: 36px; display: flex; justify-content: center; align-items: center; gap: 7px; }
  .dot { width: 14px; height: 14px; border-radius: 50%; background: var(--red); display: inline-block; }

  .contact-icon {
    position: absolute; left: 180px; width: 40px; height: 40px; border-radius: 50%;
    background: var(--red); display: flex; align-items: center; justify-content: center;
  }
  .contact-panel {
    position: absolute; left: 0; width: 100%;
    background: var(--panel); border-top: 3px solid var(--panel-edge); border-bottom: 3px solid var(--panel-edge);
    display: flex; align-items: center; justify-content: center; text-align: center; white-space: nowrap;
    color: var(--ink); font-weight: 500; font-size: 26px; line-height: 32px;
    font-variant-numeric: oldstyle-nums;
  }
  .contact-panel--phone { font-size: 29px; letter-spacing: 1px; }
  .contact-panel--email { font-size: 24px; }
</style>
</head>
<body>

<section class="card card--front">
  <div class="brand">
    <span class="brand__mark"></span>
    <span class="brand__name">Pelleway<br>Restoration LLC</span>
  </div>
  <div class="tread" style="top:438px;height:66px" role="img" aria-label="Red tire tread band"></div>
  <div class="tread" style="top:568px;height:66px" role="img" aria-label="Red tire tread band"></div>
</section>

<section class="card card--back">
  <h1 class="headline headline--title">Classic Car<br>Restoration Services</h1>
  <p class="headline headline--services">Buy <span class="dot"></span> Sell <span class="dot"></span> Trade <span class="dot"></span> Consign</p>

  <div class="tread" style="top:178px;height:46px" role="img" aria-label="Red tire tread band"></div>
  <div class="tread" style="top:270px;height:45px" role="img" aria-label="Red tire tread band"></div>

  <div class="contact-icon" style="top:342px">
    <svg width="20" height="24" viewBox="0 0 20 24"><path d="M10 0C4.5 0 1 4 1 8.5 1 15 10 24 10 24s9-9 9-15.5C19 4 15.5 0 10 0z" fill="#111"/><circle cx="10" cy="8.5" r="3.3" fill="#d21f26"/></svg>
  </div>
  <div class="contact-panel" style="top:380px;height:72px">Dorian Pelleway 4172<br>E 118th St Veyton, IL 62091</div>

  <div class="contact-icon" style="top:455px">
    <svg width="16" height="26" viewBox="0 0 16 26"><rect x="1" y="1" width="14" height="24" rx="2.5" fill="#111"/><rect x="3.5" y="4" width="9" height="15" fill="#d21f26"/><circle cx="8" cy="22" r="1.3" fill="#d21f26"/></svg>
  </div>
  <div class="contact-panel contact-panel--phone" style="top:492px;height:72px">217-555-0193</div>

  <div class="contact-icon" style="top:572px">
    <svg width="26" height="18" viewBox="0 0 26 18"><rect x="1" y="1" width="24" height="16" fill="#111"/><path d="M1 1l12 9 12-9" fill="none" stroke="#d21f26" stroke-width="2"/></svg>
  </div>
  <div class="contact-panel contact-panel--email" style="top:608px;height:72px">pellewayrestoration@mailvane.test</div>
</section>

</body>
</html>
```